I need a business Card Design for my practice , i am clinical herbalist. I am a herbalist specializing in Lyme disease, autism, autoimmune diseases, difficult to cure diseasesDifficult to cure diseases. In my innovative practice i link traditional medicine, herbs with science, immunologu ,pharmacology.

Industry/Entity Type

Business

Contact Information for Business Card

My company name : OŚRODEK ZIELNIK
My name : Piotr Kaleta
Name of my profession : Fitoterapeuta
In Polish language Fitoterapeuta is Herbalist .

e-mail: piotrkaleta@osrodekzielnik.com
www.osrodek-zielnik.pl
phone : 604 587 231
My company adress : Dąbrowa Sitnicka 41 , 38-415 Lużna
I dont have logo .

Requirements
Nice to have
• My company

```html
<!DOCTYPE html>
<html lang="pl">
<head>
<meta charset="utf-8">
<title>Ośrodek Zielnik – wizytówka</title>
<link rel="stylesheet" href="https://fonts.googleapis.com/css2?family=Oswald:wght@400;500;700&family=Rozha+One&display=swap">
<style>
  :root {
    --backdrop: #3b3b3b;
    --card-base: #d2fb7c;
    --band-bright: #a6ff00;
    --ink-blue: #0d2aa6;
    --ink-dark: #111111;
    --visual-top: #7fae4a;
    --visual-bottom: #b9793f;
  }
  * { margin: 0; padding: 0; box-sizing: border-box; }
  html, body {
    width: 1200px;
    height: 1000px;
    overflow: hidden;
    background: var(--backdrop);
  }
  .business-card {
    position: absolute;
    left: 100px;
    top: 210px;
    width: 1000px;
    height: 580px;
    background: var(--card-base);
    overflow: hidden;
    font-family: "Oswald", "Arial Narrow", sans-serif;
    color: var(--ink-dark);
  }
  .top-band {
    position: absolute;
    left: 0; top: 0;
    width: 100%; height: 20px;
    background: var(--band-bright);
  }
  .bottom-band {
    position: absolute;
    left: 0; top: 385px;
    width: 100%; height: 195px;
    background: var(--band-bright);
  }
  .herb-visual {
    position: absolute;
    left: 40px; top: 70px;
    width: 350px; height: 450px;
    background: linear-gradient(180deg, var(--visual-top) 0%, var(--visual-bottom) 100%);
  }
  .card-text {
    position: absolute;
    left: 430px; top: 50px;
    right: 30px;
  }
  .company-name {
    font-family: "Rozha One", Georgia, serif;
    font-weight: 400;
    font-size: 56px;
    line-height: 1.05;
    color: var(--ink-blue);
    letter-spacing: 1px;
    white-space: nowrap;
  }
  .profession {
    margin-top: 14px;
    font-size: 30px;
    font-weight: 400;
    line-height: 1.2;
  }
  .profession-note {
    margin-top: 8px;
    font-size: 22px;
    font-weight: 400;
    line-height: 1.2;
  }
  .person-name {
    margin-top: 56px;
    font-size: 44px;
    font-weight: 700;
    line-height: 1.1;
    color: var(--ink-blue);
    text-transform: uppercase;
    letter-spacing: 1px;
  }
  .phone {
    margin-top: 6px;
    font-size: 25px;
    font-weight: 500;
    line-height: 1.2;
    color: var(--ink-blue);
  }
  .contact-list {
    list-style: none;
    margin-top: 40px;
    font-size: 23px;
    line-height: 1.7;
  }
</style>
</head>
<body>
  <div class="business-card">
    <div class="top-band"></div>
    <div class="bottom-band"></div>
    <div class="herb-visual" role="img" aria-label="Zdjęcie: drewniany moździerz ze świeżymi ziołami"></div>
    <div class="card-text">
      <h1 class="company-name">OŚRODEK ZIELNIK</h1>
      <p class="profession">Fitoterapeuta</p>
      <p class="profession-note">In Polish language Fitoterapeuta is Herbalist</p>
      <p class="person-name">Piotr Kaleta</p>
      <p class="phone">604 587 231</p>
      <ul class="contact-list">
        <li>e-mail: piotrkaleta@osrodekzielnik.com</li>
        <li>www.osrodek-zielnik.pl</li>
        <li>Dąbrowa Sitnicka 41 , 38-415 Lużna</li>
      </ul>
    </div>
  </div>
</body>
</html>
```